Lumen award winning Hollywood sound studio needs a cool website

We need a website designed and coded to showcase our company and talent to our current and future clients. We are a post-production sound studio that works with Brindlewick, Stremora, Calloway Sons, Fablecrest, and other major Hollywood studios and companies. We primarily work designing sound effects for animated TV shows like Pebblefin Roundtoes, Kid Rockets Zoom!, Karate Otter: Lantern Riders, Fossil Realm Storm Protocol, The Odd Crew, My Aunt the Star Courier, Fire of Helios, and the recent Stremora movie Milo and the Moonlight. A website for our company would provide basic information about our studio and services, the kinds of projects we are currently working on and have worked on in the past, the awards we have won or been nominated for, and most importantly showcase our talented engineers so that producers and directors can get to know the people they might want to collaborate with. Our studio is located in Burbank, CA right in the heart of where all the studios are located. We have a basic company logo. We don't really have a color scheme to our studio so we're very open and flexible in that department. We have decorated our studio with a bit of an Art Deco style to invoke an old classy movie theater from the golden age of Hollywood. Our lobby resembles the lobby of a movie theater complete with a neon marquee where we post fun sayings or quotes from our shows. I think it would be fun for the website design to reflect that Art Deco/classic movie theater feeling. Another website that I think has a good simple design for inspiration is Marrowfield Audio: "www.marrowaudio-example.com".
Target Market(s)
Major Hollywood Studios, Animation production companies, independent film/TV production
Industry/Entity Type
Hollywood, Television, Streaming, Entertainment, Games
Coding
Coded - Design and coding required
Number of Pages Required
5+ page
Look and feel

```html
<!DOCTYPE html>
<html lang="en">
<head>
<meta charset="utf-8">
<title>Velvet Reel — Animated Sound Design Studio</title>
<link href="https://fonts.googleapis.com/css2?family=Limelight&family=Montserrat:wght@400;500;600;700&family=Oswald:wght@400;500&display=swap" rel="stylesheet">
<style>
:root{
  --bg:#151515;
  --bg-deep:#0c0c0c;
  --orange:#f3a11b;
  --green:#2f8f2c;
  --white:#f4f1ea;
  --muted:#b9b4a8;
  --tile-border:#4a4a4a;
  --display:"Limelight", serif;
  --body:"Montserrat", sans-serif;
  --condensed:"Oswald", sans-serif;
}
*{margin:0;padding:0;box-sizing:border-box}
html,body{width:1200px;height:4608px;overflow:hidden;background:var(--bg);color:var(--white);font-family:var(--body)}
.page{position:relative;width:1200px;height:4608px;overflow:hidden;
  background:radial-gradient(ellipse 500px 700px at 0 1100px,rgba(40,80,20,.35),transparent 70%),
             radial-gradient(ellipse 500px 600px at 0 3000px,rgba(50,70,20,.35),transparent 70%),
             linear-gradient(180deg,var(--bg) 0%,#131313 50%,var(--bg-deep) 100%)}
.abs{position:absolute}
.label{position:absolute;display:flex;align-items:center;gap:14px;font-size:16px;letter-spacing:3px;text-transform:uppercase;font-weight:500;color:var(--white);white-space:nowrap}
.label::before,.label::after{content:"";display:block;width:86px;height:1px;background:var(--orange)}
.display{font-family:var(--display);text-transform:uppercase;line-height:1.1;letter-spacing:3px}
.o{color:var(--orange)} .g{color:var(--green)} .w{color:var(--white)}
.btn{position:absolute;display:flex;align-items:center;justify-content:center;font-size:11px;letter-spacing:2.5px;text-transform:uppercase;font-weight:600}
.btn-solid{background:var(--orange);color:#1a1206}
.btn-ghost{border:1.5px solid var(--orange);color:var(--orange)}
.copy{font-size:12.5px;line-height:1.65;color:var(--muted)}

.hero-media{position:absolute;left:0;top:0;width:1200px;height:635px;
  background:radial-gradient(ellipse 420px 320px at 600px 120px,#3a6fc0,transparent 70%),
             radial-gradient(ellipse 500px 250px at 850px 420px,#1d4a8a,transparent 70%),
             linear-gradient(180deg,#163459 0%,#0d2340 60%,var(--bg) 100%)}
.brand{position:absolute;display:flex;align-items:center;font-family:var(--display);color:var(--white);text-transform:uppercase;text-align:center}
.hero-brand{left:500px;width:200px;top:48px;font-size:28px;line-height:1;justify-content:center;gap:8px}
.brand-mark{width:16px;height:16px;background:var(--white);flex:none}
.hero-eyebrow{left:122px;top:228px}
.hero-title{left:122px;top:292px;font-size:60px;line-height:1.06}
.hero-intro{left:796px;top:244px;width:290px;font-size:12px;line-height:1.6;color:var(--white)}

.tabs{position:absolute;left:227px;top:856px;width:752px;height:30px;display:flex;align-items:center;justify-content:space-between;background:#1d1d1d;font-size:9.5px;color:#8e8e8e;white-space:nowrap;padding-right:14px}
.tabs span{padding:0 14px;line-height:30px}
.tabs .active{background:#4a3310;color:var(--orange)}
.work-card{position:absolute;width:227px;height:262px;border-radius:12px;overflow:hidden;background:linear-gradient(180deg,#2a2414,#3b2f12)}
.work-art{height:170px}
.work-body{padding:12px 12px 0}
.work-row{display:flex;justify-content:space-between;align-items:center}
.work-title{font-family:var(--condensed);font-size:17px;text-transform:uppercase;color:var(--white)}
.pill{font-size:8.5px;color:var(--orange);border:1px solid var(--orange);border-radius:3px;padding:3px 8px;white-space:nowrap}
.work-by{font-size:9px;color:var(--muted);margin:8px 0 10px}
.work-meta{display:flex;justify-content:space-between;align-items:center;font-size:9px;color:var(--orange)}
.likes{display:flex;align-items:center;gap:6px;color:var(--white);font-size:13px;font-weight:600}

.about-art{left:560px;top:1690px;width:560px;height:400px;border-radius:24px;
  background:linear-gradient(120deg,rgba(40,90,220,.35),rgba(243,120,30,.35) 55%,rgba(190,50,150,.3))}
.about-title{left:122px;top:1770px;font-size:38px;line-height:1.35}

.service-card{position:absolute;top:2369px;width:304px;height:286px;border-radius:16px;border:2px solid #3a3a3a;background:#202020;overflow:hidden}
.service-art{margin:6px;height:230px;border-radius:12px}
.service-foot{display:flex;justify-content:space-between;align-items:center;padding:6px 12px}
.service-foot .work-title{color:var(--orange)}
.arrow{position:absolute}

.award-tile{position:absolute;width:156px;height:154px;border:1.5px solid var(--tile-border);border-radius:4px;background:#141414;display:flex;align-items:center;justify-content:center;text-align:center;font-weight:700;font-size:15px;padding:8px;line-height:1.2}
.winner{left:122px;top:3170px;text-align:left}
.winner .small{font-size:24px;color:var(--white);letter-spacing:1px}
.winner .big{font-family:var(--display);font-size:46px;color:var(--orange);line-height:1}

.testimonial-panel{position:absolute;left:122px;top:3460px;width:954px;height:500px;border-radius:30px;background:linear-gradient(180deg,#2c2c2c,#1f1f1f)}
.quote-card{position:absolute;top:3697px;width:275px;height:263px;border-radius:10px 10px 0 0;background:#1d1d1d;padding:56px 16px 0 16px}
.quote-mark{position:absolute;right:30px;top:14px;font-family:var(--display);font-size:56px;line-height:1;color:var(--orange)}
.quote-card p{font-size:11px;line-height:1.65;color:var(--muted)}
.quote-name{margin-top:16px;font-size:11px;font-weight:700;color:var(--white)}
.quote-role{font-size:11px;color:var(--orange);margin-top:4px}

.email{position:absolute;left:586px;top:4184px;width:350px;height:36px;border:1px solid #6a6a6a;font-size:9px;letter-spacing:2px;color:#9a9a9a;display:flex;align-items:center;padding-left:16px}

.footer-brand{left:0;width:1200px;top:4300px;justify-content:center;flex-direction:column;font-size:66px;line-height:.95}
.socials{position:absolute;left:518px;top:4474px;display:flex;gap:14px}
.socials span{width:30px;height:30px;border-radius:50%;background:var(--orange)}
.copyright{position:absolute;left:0;width:1200px;top:4540px;text-align:center;font-size:11px;letter-spacing:1.5px;font-weight:600}
</style>
</head>
<body>
<div class="page">

  <header class="hero">
    <div class="hero-media" role="img" aria-label="Photo of a hand mixing on a blue-lit DJ controller"></div>
    <svg class="abs" style="left:122px;top:50px" width="26" height="26" viewBox="0 0 26 26" aria-label="Search"><circle cx="11" cy="11" r="8" fill="none" stroke="#f3a11b" stroke-width="2"/><line x1="17" y1="17" x2="24" y2="24" stroke="#f3a11b" stroke-width="2"/></svg>
    <div class="brand hero-brand"><span class="brand-mark"></span><span>Velvet<br>Reel</span></div>
    <svg class="abs" style="left:1054px;top:52px" width="22" height="18" viewBox="0 0 22 18" aria-label="Menu"><rect y="0" width="22" height="2.5" fill="#f3a11b"/><rect y="7.5" width="22" height="2.5" fill="#f3a11b"/><rect y="15" width="22" height="2.5" fill="#f3a11b"/></svg>

    <div class="label hero-eyebrow">Welcome Velvet Reel</div>
    <h1 class="display abs hero-title"><span class="o">Hollywood’s<br>Go-To Studio</span><br><span class="w">For Animated<br>Sound Design</span></h1>
    <p class="abs hero-intro">Located in the heart of Hollywood, we specialize in crafting dynamic sound experiences that elevate the biggest names in animation.</p>
    <div class="btn btn-ghost" style="left:796px;top:324px;width:126px;height:34px;font-size:10px">Get in touch</div>
  </header>

  <section class="portfolio">
    <div class="label" style="left:0;width:1200px;justify-content:center;top:720px">Our Portfolio</div>
    <h2 class="display abs" style="left:0;width:1200px;text-align:center;top:770px;font-size:40px"><span class="o">Our Work</span> <span class="g">In</span> <span class="o">Action</span></h2>
    <nav class="tabs"><span class="active">Recommendation</span><span>Stremora</span><span>Brindlewick</span><span>Calloway Sons</span><span>Fablecrest</span><span>Pebblefin</span><span>Roundtoes</span><span>More</span></nav>

    <article class="work-card" style="left:122px;top:921px"><div class="work-art" role="img" aria-label="Illustration of a cartoon dinosaur in a jungle" style="background:linear-gradient(160deg,#6f8f3a,#c9b35a)"></div><div class="work-body"><div class="work-row"><span class="work-title">Brindlewick</span><span class="pill">2.45 ETH</span></div><div class="work-by">by lorem ipsum</div><div class="work-meta"><span>1 of 1 Available</span><span class="likes"><svg width="16" height="14" viewBox="0 0 16 14"><path d="M8 13 L1.8 7 A3.6 3.6 0 0 1 8 2.6 A3.6 3.6 0 0 1 14.2 7 Z" fill="none" stroke="#f4f1ea" stroke-width="1.5"/></svg>50k</span></div></div></article>
    <article class="work-card" style="left:365px;top:921px"><div class="work-art" role="img" aria-label="Illustration of a cartoon sea character on a sunny street" style="background:linear-gradient(160deg,#7fb6d8,#d8c14a)"></div><div class="work-body"><div class="work-row"><span class="work-title">Brindlewick</span><span class="pill">2.45 ETH</span></div><div class="work-by">by lorem ipsum</div><div class="work-meta"><span>1 of 1 Available</span><span class="likes"><svg width="16" height="14" viewBox="0 0 16 14"><path d="M8 13 L1.8 7 A3.6 3.6 0 0 1 8 2.6 A3.6 3.6 0 0 1 14.2 7 Z" fill="none" stroke="#f4f1ea" stroke-width="1.5"/></svg>50k</span></div></div></article>
    <article class="work-card" style="left:608px;top:921px"><div class="work-art" role="img" aria-label="Photo of a popcorn bucket on a dark stage" style="background:linear-gradient(180deg,#4a140c,#1a0b08)"></div><div class="work-body"><div class="work-row"><span class="work-title">Brindlewick</span><span class="pill">2.45 ETH</span></div><div class="work-by">by lorem ipsum</div><div class="work-meta"><span>1 of 1 Available</span><span class="likes"><svg width="16" height="14" viewBox="0 0 16 14"><path d="M8 13 L1.8 7 A3.6 3.6 0 0 1 8 2.6 A3.6 3.6 0 0 1 14.2 7 Z" fill="none" stroke="#f4f1ea" stroke-width="1.5"/></svg>50k</span></div></div></article>
    <article class="work-card" style="left:851px;top:921px"><div class="work-art" role="img" aria-label="Photo of an engineer at a microphone in a purple-lit studio" style="background:linear-gradient(160deg,#2a1f5a,#5a2a3a)"></div><div class="work-body"><div class="work-row"><span class="work-title">Brindlewick</span><span class="pill">2.45 ETH</span></div><div class="work-by">by lorem ipsum</div><div class="work-meta"><span>1 of 1 Available</span><span class="likes"><svg width="16" height="14" viewBox="0 0 16 14"><path d="M8 13 L1.8 7 A3.6 3.6 0 0 1 8 2.6 A3.6 3.6 0 0 1 14.2 7 Z" fill="none" stroke="#f4f1ea" stroke-width="1.5"/></svg>50k</span></div></div></article>

    <article class="work-card" style="left:122px;top:1202px"><div class="work-art" role="img" aria-label="Illustration of a child riding a green dragon" style="background:linear-gradient(160deg,#6aa8d8,#3f8a5a)"></div><div class="work-body"><div class="work-row"><span class="work-title">Brindlewick</span><span class="pill">2.45 ETH</span></div><div class="work-by">by lorem ipsum</div><div class="work-meta"><span>1 of 1 Available</span><span class="likes"><svg width="16" height="14" viewBox="0 0 16 14"><path d="M8 13 L1.8 7 A3.6 3.6 0 0 1 8 2.6 A3.6 3.6 0 0 1 14.2 7 Z" fill="none" stroke="#f4f1ea" stroke-width="1.5"/></svg>50k</span></div></div></article>
    <article class="work-card" style="left:365px;top:1202px"><div class="work-art" role="img" aria-label="Illustration of a figure watching a starry night sky" style="background:linear-gradient(180deg,#0d1a3a,#2a4a8a)"></div><div class="work-body"><div class="work-row"><span class="work-title">Brindlewick</span><span class="pill">2.45 ETH</span></div><div class="work-by">by lorem ipsum</div><div class="work-meta"><span>1 of 1 Available</span><span class="likes"><svg width="16" height="14" viewBox="0 0 16 14"><path d="M8 13 L1.8 7 A3.6 3.6 0 0 1 8 2.6 A3.6 3.6 0 0 1 14.2 7 Z" fill="none" stroke="#f4f1ea" stroke-width="1.5"/></svg>50k</span></div></div></article>
    <article class="work-card" style="left:608px;top:1202px"><div class="work-art" role="img" aria-label="Illustration of animated children in a park" style="background:linear-gradient(160deg,#8a9a5a,#c8a060)"></div><div class="work-body"><div class="work-row"><span class="work-title">Brindlewick</span><span class="pill">2.45 ETH</span></div><div class="work-by">by lorem ipsum</div><div class="work-meta"><span>1 of 1 Available</span><span class="likes"><svg width="16" height="14" viewBox="0 0 16 14"><path d="M8 13 L1.8 7 A3.6 3.6 0 0 1 8 2.6 A3.6 3.6 0 0 1 14.2 7 Z" fill="none" stroke="#f4f1ea" stroke-width="1.5"/></svg>50k</span></div></div></article>
    <article class="work-card" style="left:851px;top:1202px"><div class="work-art" role="img" aria-label="Illustration of two children under a glowing night sky" style="background:linear-gradient(180deg,#1a3a7a,#c0602a)"></div><div class="work-body"><div class="work-row"><span class="work-title">Brindlewick</span><span class="pill">2.45 ETH</span></div><div class="work-by">by lorem ipsum</div><div class="work-meta"><span>1 of 1 Available</span><span class="likes"><svg width="16" height="14" viewBox="0 0 16 14"><path d="M8 13 L1.8 7 A3.6 3.6 0 0 1 8 2.6 A3.6 3.6 0 0 1 14.2 7 Z" fill="none" stroke="#f4f1ea" stroke-width="1.5"/></svg>50k</span></div></div></article>

    <div class="btn btn-solid" style="left:466px;top:1522px;width:126px;height:38px">View all</div>
    <div class="btn btn-ghost" style="left:608px;top:1522px;width:126px;height:38px">Get in touch</div>
  </section>

  <section class="about">
    <div class="abs about-art" role="img" aria-label="Illustration of a glowing speaker surrounded by music notes"></div>
    <div class="label" style="left:122px;top:1717px">About Our Journy</div>
    <h2 class="display abs about-title"><span class="o">Bringing Stories</span><br><span class="o">To</span> <span class="g">Life</span> <span class="o">Through</span><br><span class="g">Sound</span></h2>
    <p class="abs copy" style="left:122px;top:1960px;width:282px">At the heart of Hollywood’s animation scene, our Lumen-winning studio brings sound to life. From iconic sound effects to immersive audio landscapes, we collaborate with the biggest names in the industry to create unforgettable auditory experiences</p>
    <p class="abs copy" style="left:424px;top:1960px;width:284px">Our Burbank-based sound studio is home to Lumen-winning engineers who design the sounds behind Hollywood’s most iconic animations. We are driven by a passion for sound that transforms animated stories into cinematic experiences.</p>
    <div class="btn btn-ghost" style="left:424px;top:2089px;width:126px;height:36px">Read more</div>
  </section>

  <section class="services">
    <div class="label" style="left:0;width:1200px;justify-content:center;top:2238px">Our Services</div>
    <h2 class="display abs" style="left:0;width:1200px;text-align:center;top:2294px;font-size:40px"><span class="o">What We</span> <span class="g">Do</span></h2>
    <svg class="arrow" style="left:78px;top:2497px" width="26" height="18" viewBox="0 0 26 18" aria-label="Previous"><path d="M25 9H3M10 2L3 9l7 7" fill="none" stroke="#f3a11b" stroke-width="2"/></svg>
    <article class="service-card" style="left:122px"><div class="service-art" role="img" aria-label="Photo of a mixing console with blue screens" style="background:linear-gradient(160deg,#2a5a8a,#0e1a2a)"></div><div class="service-foot"><span class="work-title">Sound Design</span><span class="pill">2.45 ETH</span></div></article>
    <article class="service-card" style="left:447px"><div class="service-art" role="img" aria-label="Photo of engineers working at a recording desk" style="background:linear-gradient(160deg,#4a4a4a,#1a1a1a)"></div><div class="service-foot"><span class="work-title">Mixing</span><span class="pill">2.45 ETH</span></div></article>
    <article class="service-card" style="left:772px"><div class="service-art" role="img" aria-label="Photo of a foley artist with audio equipment" style="background:linear-gradient(160deg,#8a4a1a,#1a1210)"></div><div class="service-foot"><span class="work-title">Foley</span><span class="pill">2.45 ETH</span></div></article>
    <svg class="arrow" style="left:1100px;top:2495px" width="42" height="22" viewBox="0 0 42 22" aria-label="Next"><path d="M1 11h38M30 2l9 9-9 9" fill="none" stroke="#f3a11b" stroke-width="2.5"/></svg>
    <div class="btn btn-solid" style="left:537px;top:2687px;width:126px;height:36px">View all</div>
  </section>

  <section class="awards">
    <div class="label" style="left:122px;top:2829px">Award-Winning Excellence</div>
    <h2 class="display abs" style="left:122px;top:2882px;font-size:38px;line-height:1.25"><span class="o">Celebrating</span><br><span class="o">Excellence</span> <span class="g">In Sound</span></h2>
    <p class="abs copy" style="left:676px;top:2826px;width:400px;font-size:11.5px;color:var(--white)">From Lumen Awards to industry accolades, our work is recognized for pushing the boundaries of animated sound. We are honored to collaborate with leading studios to bring extraordinary sound to life. With multiple Lumen wins and nominations, our studio’s soundscapes continue to set the standard in Hollywood’s animation industry.</p>
    <div class="abs" role="img" aria-label="Golden award statuette" style="left:182px;top:3080px;width:50px;height:84px;background:linear-gradient(180deg,#c9a04a,#6a4e1a);opacity:.8"></div>
    <div class="abs winner"><div class="small">LUMEN AWARD</div><div class="big">WINNER</div></div>
    <div class="btn btn-solid" style="left:186px;top:3320px;width:125px;height:36px">View all</div>

    <div class="award-tile" style="left:399px;top:3013px;color:#e0362a">Stremora</div>
    <div class="award-tile" style="left:572px;top:3031px;color:var(--orange)">Brindlewick</div>
    <div class="award-tile" style="left:747px;top:3031px;color:#3a7be0">Calloway Sons</div>
    <div class="award-tile" style="left:921px;top:3031px;color:var(--white)">Fablecrest</div>
    <div class="award-tile" style="left:399px;top:3200px;color:#e8d23a">Pebblefin Roundtoes</div>
    <div class="award-tile" style="left:572px;top:3200px;color:#e8d23a">Kid Rockets Zoom!</div>
    <div class="award-tile" style="left:747px;top:3200px;color:var(--orange)">The Odd Crew</div>
    <div class="award-tile" style="left:921px;top:3200px;color:var(--orange)">Brindlewick</div>
  </section>

  <section class="testimonials">
    <div class="testimonial-panel"></div>
    <div class="label" style="left:0;width:1200px;justify-content:center;top:3527px">Testimonial</div>
    <h2 class="display abs" style="left:0;width:1200px;text-align:center;top:3574px;font-size:36px;line-height:1.15"><span class="o">Hear What The</span><br><span class="w">Industry Has To Say</span></h2>
    <svg class="arrow" style="left:80px;top:3818px" width="34" height="20" viewBox="0 0 34 20" aria-label="Previous"><path d="M33 10H3M11 2l-8 8 8 8" fill="none" stroke="#f3a11b" stroke-width="2.5"/></svg>
    <article class="quote-card" style="left:156px"><span class="quote-mark">”</span><p>Lorem Ipsum has been the industry’s standard dummy text ever since the 1500s, when an unknown printer took a galley of type and scrambled it to make a type specimen book. Lorem Ipsum is simply dummy text of the printing and typesetting industry.</p><div class="quote-name">JHON SIHGN</div><div class="quote-role">Customer</div></article>
    <article class="quote-card" style="left:458px"><span class="quote-mark">”</span><p>Lorem Ipsum has been the industry’s standard dummy text ever since the 1500s, when an unknown printer took a galley of type and scrambled it to make a type specimen book. Lorem Ipsum is simply dummy text of the printing and typesetting industry.</p><div class="quote-name">JHON SIHGN</div><div class="quote-role">Customer</div></article>
    <article class="quote-card" style="left:760px"><span class="quote-mark">”</span><p>Lorem Ipsum has been the industry’s standard dummy text ever since the 1500s, when an unknown printer took a galley of type and scrambled it to make a type specimen book. Lorem Ipsum is simply dummy text of the printing and typesetting industry.</p><div class="quote-name">JHON SIHGN</div><div class="quote-role">Customer</div></article>
    <svg class="arrow" style="left:1090px;top:3818px" width="34" height="20" viewBox="0 0 34 20" aria-label="Next"><path d="M1 10h30M23 2l8 8-8 8" fill="none" stroke="#f3a11b" stroke-width="2.5"/></svg>
  </section>

  <section class="newsletter">
    <div class="label" style="left:122px;top:4034px">Newsletter Subscription</div>
    <h2 class="display abs" style="left:122px;top:4092px;font-size:38px;line-height:1.25"><span class="o">Subscribe Our</span><br><span class="g">Newsletter</span></h2>
    <p class="abs copy" style="left:586px;top:4102px;width:490px;font-size:11.5px;color:var(--white)">Our Burbank-based sound studio is home to Lumen-winning engineers who design the sounds behind Hollywood’s most iconic animations. We are driven by a passion for sound that transforms animated stories into cinematic experiences.</p>
    <div class="email">ENTER YOUR EMAIL</div>
    <div class="btn btn-solid" style="left:951px;top:4184px;width:124px;height:36px">Subscribe</div>
  </section>

  <footer class="footer">
    <div class="brand footer-brand"><span class="brand-mark" style="width:24px;height:24px;margin-bottom:10px"></span><span>Velvet<br>Reel</span></div>
    <div class="socials"><span role="img" aria-label="Social link"></span><span role="img" aria-label="Social link"></span><span role="img" aria-label="Social link"></span><span role="img" aria-label="Social link"></span></div>
    <p class="copyright">© COPYRIGHT ALL RIGHT RESERVED 2024. VELVET REEL</p>
  </footer>

</div>
</body>
</html>
```